Flyer für Hausreinigung
Zielgruppe
Hausverwaltungen, Hausbesitzer.
Aufgabenstellung
Ergebnis soll ein Winword-Dokument mit einem Firmenlogo (Vorschlag: Tintenklecks hellgrün/blau verlaufend mit orangem Besen/Wischer/oder Hand - andere Ideen sind willkommen!) sein, das ich noch um Firmenname/Adresse bzw. Empfängerdaten noch vervollständigen/individualisieren kann. Es soll bunt, aber nicht überladen sein, eventuell mit Stockfotos von lachenden/glücklich schauenden aktiven Menschen sein, jung dynamisch aber nicht flippig. Folgender Text sollte darin vorkommen, Umformulierungen und andere Ideen sind hochwillkommen:
Unser Ziel ist es eine Hausbetreuung fast wie ein Hausbesorger zu leisten, jedoch mit zusätzlichen Vorteilen:
· Der Vertrag ist jederzeit ohne Frist kündbar, ohne Angabe von Gründen!
· Reinigung 1 x pro Woche sowie zusätzliche Bedarfsreinigung
· Krankheits- und Urlaubsvertretung sind bereits inklusive.
· Haftpflichtversicherung über 1,5 Mio. Euro
· Inklusive Gartenbetreuung, Garage, Dachboden, Haustechnik
· Kontrollgänge, 7 x 24 h Erreichbarkeit für Mieter und Eigentümer, Handwerkerüberwachung, Notfallkoordination
· Winterbetreuung der Gehsteige täglich mindestens zwischen 6:00 und 22:00
· Inklusive aller Hilfsmittel und Materialien
· Fixpreis pro Monat.
Nach Möglichkeit soll das auf 1 A4-Seite Platz finden.

```html
<!DOCTYPE html>
<html lang="de">
<head>
<meta charset="utf-8">
<title>Anton Berger Hausbetreuung – Flyer</title>
<link href="https://fonts.googleapis.com/css2?family=Open+Sans:ital,wght@0,700;1,600;1,700;1,800&display=swap" rel="stylesheet">
<style>
  :root {
    --sky-top: #2fa3de;
    --sky-mid: #8fd0f0;
    --sky-pale: #dcf0fa;
    --paper: #f4fafd;
    --ink: #111111;
    --ink-footer: #1d2b38;
    --footer-band: #a9d3ea;
    --photo-warm: #b4733f;
    --photo-light: #eef1f0;
    --photo-wood: #6a3a1e;
    --brand: #1a1a1a;
    --brand-square: #f2c316;
  }
  * { margin: 0; padding: 0; box-sizing: border-box; }
  html, body { width: 848px; height: 1200px; overflow: hidden; }
  body {
    position: relative;
    font-family: "Open Sans", Arial, sans-serif;
    background: linear-gradient(180deg, var(--sky-top) 0px, var(--sky-mid) 170px, var(--sky-pale) 330px, var(--paper) 560px, var(--paper) 100%);
  }
  .wave { position: absolute; left: 0; top: 150px; width: 848px; height: 160px; }
  .brand {
    position: absolute; left: 283px; top: 112px;
    display: flex; align-items: center; gap: 12px;
  }
  .brand-square { width: 66px; height: 66px; background: var(--brand-square); }
  .brand-name { font-weight: 700; font-size: 34px; color: var(--brand); line-height: 1; }
  .brand-tag { font-weight: 700; font-size: 12px; color: var(--brand); margin-top: 4px; }
  .pitch {
    position: absolute; left: 55px; top: 296px; width: 790px;
    transform: rotate(2.5deg); transform-origin: left top;
    color: var(--ink);
    text-shadow: 2px 3px 4px rgba(0,0,0,.35);
  }
  .headline {
    font-style: italic; font-weight: 800; font-size: 24px; line-height: 1.55;
    white-space: nowrap;
  }
  .headline span { display: block; padding-left: 22px; }
  .benefits {
    list-style: none; margin: 26px 0 0 42px; width: 560px;
    font-style: italic; font-weight: 600; font-size: 19px; line-height: 1.22;
  }
  .benefits li::before { content: "· "; }
  .photo {
    position: absolute; left: 0; top: 745px; width: 848px; height: 455px;
    background:
      linear-gradient(180deg, rgba(238,241,240,0) 0%, rgba(180,115,63,.55) 75%, var(--photo-wood) 100%),
      linear-gradient(90deg, var(--photo-wood) 0%, var(--photo-warm) 28%, var(--photo-light) 52%, var(--photo-light) 100%);
  }
  .contact-band {
    position: absolute; left: 0; top: 1096px; width: 848px; height: 64px;
    background: var(--footer-band);
    font-style: italic; font-weight: 700; font-size: 17px; color: var(--ink-footer);
  }
  .contact-band span { position: absolute; top: 21px; white-space: nowrap; }
  .contact-street { left: 194px; }
  .contact-city { left: 294px; }
  .contact-phone { left: 422px; }
  .contact-mail { left: 589px; }
</style>
</head>
<body>
  <svg class="wave" viewBox="0 0 848 160" preserveAspectRatio="none" aria-hidden="true">
    <path d="M0 70 C220 0 520 120 848 40 L848 160 L0 160 Z" fill="#ffffff" opacity=".55"/>
    <path d="M0 105 C240 40 540 150 848 80 L848 160 L0 160 Z" fill="var(--sky-pale)"/>
  </svg>

  <header class="brand">
    <div class="brand-square"></div>
    <div>
      <div class="brand-name">Anton Berger</div>
      <div class="brand-tag">Hausbetreuung</div>
    </div>
  </header>

  <div class="photo" role="img" aria-label="Foto eines hellen, modernen Wohnraums mit Holzboden, großen Fenstern, Sofa und Zimmerpflanze"></div>

  <section class="pitch">
    <h1 class="headline">Unser Ziel ist es eine Hausbetreuung fast wie ein<span>Hausbesorger zu leisten, jedoch mit zusätzlichen Vorteilen:</span></h1>
    <ul class="benefits">
      <li>Der Vertrag ist jederzeit ohne Frist kündbar, ohne Angabe von Gründen!</li>
      <li>Reinigung 1 x pro Woche sowie zusätzliche Bedarfsreinigung</li>
      <li>Krankheits- und Urlaubsvertretung sind bereits inklusive.</li>
      <li>Haftpflichtversicherung über 1,5 Mio. Euro</li>
      <li>Inklusive Gartenbetreuung, Garage, Dachboden, Haustechnik</li>
      <li>Kontrollgänge, 7 x 24 h Erreichbarkeit für Mieter und Eigentümer, Handwerkerüberwachung, Notfallkoordination</li>
      <li>Winterbetreuung der Gehsteige täglich mindestens zwischen 6:00 und 22:00</li>
      <li>Inklusive aller Hilfsmittel und Materialien</li>
      <li>Fixpreis pro Monat.</li>
    </ul>
  </section>

  <footer class="contact-band">
    <span class="contact-street">Lindenweg 4</span>
    <span class="contact-city">Musterstadt</span>
    <span class="contact-phone">Tel: 0123456789</span>
    <span class="contact-mail">Email: info@berger.at</span>
  </footer>
</body>
</html>
```